The Molar Ledger (Cover Design for Ebook)

I need a cool and exciting eBook cover for my new book, launching very soon!
I want it to stand out and appeal to young professionals with big dreams.
It should be dramatic and bold and avoid cliche or generic photos. Simple design will work as long as it relates to the message of the book. The content will provide ten years of experience from working in the field and achieving success.
Title: The Molar Ledger (at the top)
(Subheading Updated) The secrets to money, motivation and success they don’t teach you in dental school
OR The secrets to success they don't teach you in dental school.
OR The secrets to money, motivation and success
(smaller under title)
Author Updated: Dr K Fenwick (place at the bottom)
Updates

Target Market(s)

Ambitious young dentists
See instagram www.snapverse.net/themolarledger for a sense of the style that I think could work.

Font styles to use
Serif
Sans Serif

Colors

Designer to choose colors to be used in the design.

Requirements
Must have
• Eye catching and cool.
• Show the benefits of success. Money, freedom, luxury
• Clear title and subheading
Nice to have
• Subtle dental reference
• dimensions 1600x2400
Should not have
• Boring photos of dentist/patients, dental clinic, teeth etc,

```html
<!DOCTYPE html>
<html lang="en">
<head>
<meta charset="utf-8">
<title>The Molar Ledger — Cover</title>
<link rel="stylesheet" href="https://fonts.googleapis.com/css2?family=Oswald:wght@300;500;700&display=swap">
<style>
  :root {
    --sky-top: #8dd5d6;
    --sky-fade: #ffffff;
    --ink: #111111;
    --doll-teal: #5fc7c3;
    --doll-red: #d9423f;
    --doll-cream: #f1e6dc;
  }
  html, body {
    margin: 0;
    padding: 0;
    overflow: hidden;
    background: #ffffff;
  }
  .cover {
    position: relative;
    width: 848px;
    height: 1200px;
    overflow: hidden;
    background: linear-gradient(180deg, var(--sky-top) 0%, #bfe7e7 22%, var(--sky-fade) 44%, var(--sky-fade) 100%);
    font-family: "Oswald", "Arial Narrow", sans-serif;
    color: var(--ink);
  }
  .cover-type {
    position: absolute;
    inset: 0;
    width: 848px;
    height: 1200px;
  }
  .series-title { font-weight: 500; font-size: 82px; }
  .headline { font-weight: 700; }
  .author { font-weight: 300; font-size: 58px; letter-spacing: 4px; }
  .rule { stroke: var(--ink); stroke-width: 3; }
  .doll-lineup {
    position: absolute;
    left: 113px;
    top: 812px;
    width: 603px;
    height: 296px;
    border-radius: 140px 140px 30px 30px / 120px 120px 20px 20px;
    background:
      radial-gradient(ellipse 28% 60% at 18% 55%, var(--doll-teal) 0%, rgba(95,199,195,0) 100%),
      radial-gradient(ellipse 22% 50% at 44% 60%, var(--doll-teal) 0%, rgba(95,199,195,0) 100%),
      radial-gradient(ellipse 16% 40% at 64% 66%, var(--doll-red) 0%, rgba(217,66,63,0) 100%),
      radial-gradient(ellipse 10% 28% at 82% 74%, var(--doll-teal) 0%, rgba(95,199,195,0) 100%),
      linear-gradient(180deg, #ffffff 0%, var(--doll-cream) 100%);
  }
</style>
</head>
<body>
  <main class="cover">
    <svg class="cover-type" viewBox="0 0 848 1200" xmlns="http://www.w3.org/2000/svg" fill="#111111">
      <text class="series-title" x="38" y="137" textLength="752" lengthAdjust="spacing">THE MOLAR LEDGER</text>
      <line class="rule" x1="38" y1="171" x2="802" y2="171"/>
      <text class="headline" x="38" y="300" font-size="118" textLength="715" lengthAdjust="spacingAndGlyphs">THE SECRETS TO</text>
      <text class="headline" x="48" y="468" font-size="180" textLength="714" lengthAdjust="spacing">MONEY</text>
      <text class="headline" x="50" y="565" font-size="88" textLength="694" lengthAdjust="spacingAndGlyphs">MOTIVATION&#160;&#160;AND</text>
      <text class="headline" x="45" y="671" font-size="107" textLength="699" lengthAdjust="spacing">SUCCESS</text>
      <line class="rule" x1="38" y1="725" x2="802" y2="725"/>
      <text class="author" x="790" y="802" text-anchor="end">by Kit Fenwick</text>
    </svg>
    <div class="doll-lineup" role="img" aria-label="Photograph of five nesting dolls in a row, painted as a dentist with pliers and a tooth, an assistant holding an X-ray, a patient with toothache, a child, and a tiny tooth"></div>
  </main>
</body>
</html>
```